WordPress Site Clean up

We are a small wireless networking company in Norther Colorado. We have a basic layout to our new website, and require a person or persons who can clean the new site up so we can go live with it in the coming weeks. Our company has the logo and content, we just need to clean the formatting up, improve the colors/graphics. It is currently a PLIXORA. We also need help making our project pictures look better on the website, and clean up the images all around.

The website can be found at: www.7kqairgrid.com/newsite

We can provide you with photos and more content, but we have gone as far as we can with "building" the wordpress site.

It Company

```html
<!DOCTYPE html>
<html lang="en">
<head>
<meta charset="utf-8">
<title>7kQ Airgrid — Wireless Networks</title>
<link href="https://fonts.googleapis.com/css2?family=Open+Sans:wght@400;600;700&family=Oswald:wght@400;500&display=swap" rel="stylesheet">
<style>
:root{
  --green:#6ea52a;
  --green-dark:#55861b;
  --ink:#333;
  --muted:#888;
  --line:#e4e4e4;
  --hero:#c9c09a;
  --white:#fff;
  --dark-btn:#3d3d3d;
}
*{box-sizing:border-box;margin:0;padding:0}
html,body{width:776px;height:1200px;overflow:hidden;background:var(--white)}
body{font-family:"Open Sans",Arial,sans-serif;color:var(--ink);font-size:9px;line-height:1.4;position:relative}
.topbar{height:20px;background:var(--green-dark);color:#e8f2d8;display:flex;align-items:center;gap:16px;padding:0 40px;font-size:8px}
.topbar span{display:flex;align-items:center;gap:4px}
.header{height:52px;display:flex;align-items:center;justify-content:space-between;padding:0 40px;border-bottom:1px solid var(--line)}
.brand{display:flex;align-items:center;gap:6px;font-weight:700;font-size:20px;color:var(--green-dark)}
.brand i{width:12px;height:12px;background:var(--green);display:block}
.nav{display:flex;gap:14px;font-size:8px;font-weight:600;text-transform:uppercase}
.nav a{color:var(--ink);text-decoration:none}
.nav a.active{color:var(--green)}
.hero{position:absolute;top:72px;left:0;width:776px;height:295px;background:var(--hero)}
.hero-photo{position:absolute;right:40px;top:0;width:380px;height:295px;background:linear-gradient(120deg,#d8cfac,#b9a982 60%,#9e8f6a)}
.hero-copy{position:absolute;left:70px;top:34px}
.hero-copy .l1{font-family:"Oswald",sans-serif;font-size:28px;color:var(--white);letter-spacing:.5px;line-height:1}
.hero-copy .l2{display:inline-block;margin-top:4px;background:var(--green);color:var(--white);font-family:"Oswald",sans-serif;font-size:26px;padding:2px 8px;line-height:1.1}
.hero-copy p{margin-top:8px;width:250px;color:var(--white);font-weight:600;font-size:9px}
.hero-copy .more{display:inline-block;margin-top:10px;background:#4a4a4a;color:var(--white);font-size:7px;padding:4px 8px}
.features{position:absolute;top:280px;left:100px;width:580px;height:260px;display:flex;gap:20px}
.feature-card{width:170px;height:258px;background:var(--white);border:2px solid var(--green);padding:6px;text-align:center}
.feature-card .img{height:140px;background:linear-gradient(#cfd8e0,#a89a80)}
.feature-card p{font-size:7px;color:var(--muted);margin:12px 4px}
.btn-outline{display:inline-block;border:1px solid var(--green);color:var(--green);font-size:7px;padding:4px 10px}
.feature{flex:1;text-align:center;padding-top:170px}
.feature svg{display:block;margin:0 auto 4px}
.feature h3{font-size:10px;font-weight:700}
.feature p{font-size:7px;color:var(--muted);margin-top:4px}
.section-title{position:absolute;left:0;width:776px;text-align:center;font-family:"Oswald",sans-serif;font-size:18px;text-transform:uppercase;font-weight:400}
.section-title b{color:var(--green);font-weight:400}
.section-title::before,.section-title::after{content:"";display:inline-block;width:90px;height:1px;background:var(--line);vertical-align:middle;margin:0 12px}
.services{position:absolute;top:640px;left:100px;width:580px;display:grid;grid-template-columns:repeat(3,1fr);row-gap:44px;column-gap:20px}
.service{display:flex;gap:8px}
.service .ico{width:30px;height:30px;background:var(--green);flex:none;display:flex;align-items:center;justify-content:center}
.service h4{font-size:8px;font-weight:700;text-transform:uppercase}
.service p{font-size:7px;color:var(--muted)}
.left-title{position:absolute;left:100px;font-family:"Oswald",sans-serif;font-size:16px;text-transform:uppercase;font-weight:500}
.left-title b{color:var(--green);font-weight:500}
.left-title::after{content:"";display:block;width:30px;height:2px;background:var(--green);margin-top:2px}
.projects{position:absolute;top:846px;left:100px;width:580px;display:flex;gap:6px;height:112px}
.project{flex:1}
.project.lead{background:var(--green);color:var(--white);padding:10px}
.project.lead h5{font-size:9px;font-weight:700;text-transform:uppercase}
.project.lead p{font-size:7px;margin:6px 0}
.project.lead span{display:inline-block;background:var(--dark-btn);font-size:7px;padding:3px 7px}
.ph1{background:linear-gradient(#bfd0de,#8a8a80)}
.ph2{background:linear-gradient(#cfdbe6,#9b9588)}
.ph3{background:linear-gradient(#b7c9d8,#7f8a8c)}
.blog{position:absolute;top:1017px;left:100px;width:360px;height:92px;background:linear-gradient(90deg,#9cbf6a,#8a9c8c)}
.blog .tag{position:absolute;left:8px;top:8px;width:120px;background:var(--green);color:var(--white);padding:8px}
.blog .tag h5{font-size:9px;font-weight:700}
.blog .tag p{font-size:7px;margin-top:4px}
.dots{position:absolute;top:1120px;left:100px;display:flex;gap:4px}
.dots i{width:7px;height:7px;border-radius:50%;background:#ccc;display:block}
.dots i:first-child{background:var(--green)}
.testimonial{position:absolute;top:1017px;left:500px;width:180px}
.testimonial .quote{font-family:"Oswald",sans-serif;font-size:28px;color:var(--green);line-height:.8;float:left;margin-right:4px}
.testimonial p{font-size:7px;color:var(--muted);font-style:italic}
.testimonial .who{margin-top:8px;display:flex;align-items:center;gap:6px;font-size:7px;color:var(--green)}
.testimonial .who i{width:20px;height:20px;background:#b8a890;display:block}
.footer-brand{position:absolute;top:1138px;right:96px;text-align:right}
.footer-brand .brand{justify-content:flex-end;font-size:16px}
.footer-brand small{display:block;font-size:6px;color:var(--muted)}
</style>
</head>
<body>
<div class="topbar">
  <span><svg width="8" height="8" viewBox="0 0 10 10"><path d="M2 1l2 2-1 1.5c.6 1.2 1.4 2 2.5 2.5L7 6l2 2-1.5 1.5C4.5 9 1 5.5.5 2.5z" fill="#e8f2d8"/></svg>Toll Free: (970) 555-0142</span>
  <span><svg width="9" height="7" viewBox="0 0 10 8"><rect x=".5" y=".5" width="9" height="7" fill="none" stroke="#e8f2d8"/><path d="M.5.5l4.5 4 4.5-4" fill="none" stroke="#e8f2d8"/></svg>info@7kqairgrid.com</span>
</div>
<header class="header">
  <div class="brand"><i></i>7kQ Airgrid</div>
  <nav class="nav"><a class="active">Home</a><a>About 7kQ</a><a>Markets</a><a>Services</a><a>Products</a><a>Testimonials</a><a>Technologies</a><a>Contact</a></nav>
</header>

<section class="hero">
  <div class="hero-photo" role="img" aria-label="Photo of smiling students holding a tablet"></div>
  <div class="hero-copy">
    <div class="l1">SMARTEST WIRELESS</div>
    <div class="l2">FOR EDUCATIONS</div>
    <p>Fast reliable links for every campus, school and classroom across the region today.</p>
    <span class="more">Learn More</span>
  </div>
</section>

<section class="features">
  <div class="feature-card">
    <div class="img" role="img" aria-label="Photo of company office building"></div>
    <p>Founded in 2003, our network team has served local towns and schools with care and speed.</p>
    <span class="btn-outline">Show More Details</span>
  </div>
  <div class="feature">
    <svg width="22" height="22" viewBox="0 0 22 22"><circle cx="11" cy="11" r="10" fill="#6ea52a"/><path d="M6 11l3 3 7-7" stroke="#fff" stroke-width="2" fill="none"/></svg>
    <h3>Solutions</h3>
    <p>We are a wireless networking provider. We carefully learn the needs of our customers and fit them with the right solution.</p>
  </div>
  <div class="feature">
    <svg width="22" height="22" viewBox="0 0 22 22"><circle cx="11" cy="11" r="10" fill="#6ea52a"/><path d="M7 15l8-8M12 7h3v3" stroke="#fff" stroke-width="2" fill="none"/></svg>
    <h3>Design</h3>
    <p>Designing networks is a mix of science, standards and a little bit of art. Many ISPs can sell you the equipment.</p>
  </div>
</section>

<h2 class="section-title" style="top:578px">Our Most <b>Populer</b> Service</h2>
<section class="services">
  <div class="service"><div class="ico"><svg width="14" height="14" viewBox="0 0 14 14"><rect x="2" y="2" width="10" height="10" fill="none" stroke="#fff" stroke-width="1.5"/></svg></div><div><h4>Planning and Design</h4><p>Lorem ipsum dolor sit amet, consectetur adipiscing elit.</p></div></div>
  <div class="service"><div class="ico"><svg width="14" height="14" viewBox="0 0 14 14"><path d="M2 10l4-4 3 3 4-5" stroke="#fff" stroke-width="1.5" fill="none"/></svg></div><div><h4>Equipment Sales</h4><p>Lorem ipsum dolor sit amet, consectetur adipiscing elit.</p></div></div>
  <div class="service"><div class="ico"><svg width="14" height="14" viewBox="0 0 14 14"><path d="M7 1v12M3 5l4-4 4 4" stroke="#fff" stroke-width="1.5" fill="none"/></svg></div><div><h4>Install</h4><p>Lorem ipsum dolor sit amet, consectetur adipiscing elit.</p></div></div>
  <div class="service"><div class="ico"><svg width="14" height="14" viewBox="0 0 14 14"><circle cx="7" cy="7" r="5" stroke="#fff" stroke-width="1.5" fill="none"/></svg></div><div><h4>Implementation</h4><p>Lorem ipsum dolor sit amet, consectetur adipiscing elit.</p></div></div>
  <div class="service"><div class="ico"><svg width="14" height="14" viewBox="0 0 14 14"><path d="M1 7h3l2-4 2 8 2-4h3" stroke="#fff" stroke-width="1.5" fill="none"/></svg></div><div><h4>Management &amp; Monitoring</h4><p>Lorem ipsum dolor sit amet, consectetur adipiscing elit.</p></div></div>
  <div class="service"><div class="ico"><svg width="14" height="14" viewBox="0 0 14 14"><path d="M3 11l6-6M8 2l4 4" stroke="#fff" stroke-width="1.5" fill="none"/></svg></div><div><h4>Maintenance</h4><p>Lorem ipsum dolor sit amet, consectetur adipiscing elit.</p></div></div>
</section>

<h2 class="left-title" style="top:800px">Our Latest <b>Projects</b></h2>
<section class="projects">
  <div class="project lead"><h5>Skyvault Relay 1.5 Gbps</h5><p>Our new licensed backhaul link now runs at full gigabit speed.</p><span>Read More</span></div>
  <div class="project ph1" role="img" aria-label="Photo of rooftop antenna installation"></div>
  <div class="project ph2" role="img" aria-label="Photo of wireless tower equipment"></div>
  <div class="project ph3" role="img" aria-label="Photo of radio dishes on a roof"></div>
</section>

<h2 class="left-title" style="top:978px">Latest From <b>Blog</b></h2>
<h2 class="left-title" style="top:978px;left:500px"><b>Testimonials</b></h2>
<section class="blog" role="img" aria-label="Photo of wireless equipment on a building">
  <div class="tag"><h5>Building Wireless</h5><p>Notes from our latest rooftop site build.</p></div>
</section>
<div class="dots"><i></i><i></i><i></i><i></i><i></i></div>
<section class="testimonial">
  <span class="quote">“</span>
  <p>Lorem ipsum dolor sit amet, consectetur adipiscing elit. Proin dignissim viverra nunc, vitae feugiat purus tempor in. Sed blandit risus.</p>
  <div class="who"><i role="img" aria-label="Customer portrait"></i>— Lena Ortvik</div>
</section>
<div class="footer-brand">
  <div class="brand"><i></i>7kQ Airgrid</div>
  <small>Copyright 2015 7kQ Airgrid</small>
</div>
</body>
</html>
```